Landing page for new software as a service product

==== ENGLISH VERSION ====

Due to our excellent customer service, the company FernHaven has gained many satisfied customers. Now we have developed a new product, which enables companies in times of Covid-19 to use a video salesroom, to get in contact with their customers. In contrast to many other solutions on the market, it is not only an outbound solution. Our solution can handle incoming calls from the website / shop / app of a customer. The video call is routed by different rules (regarding day of week, time and sales agent) to the correct sales agent. If no sales agent is available different exit strategies are available to not loose the lead.

We need a LANDING PAGE for this application (no backend design!), Which can later be translated into different languages. Attached are screenshots of the application, which can be used if required. If you need other information, you are free to contact us and we try to provide these information to you.

==== GERMAN VERSION ====

As a cloud provider, FernHaven has gained many satisfied customers through excellent customer service in recent years. Now we have developed a new product that enables companies to make sales via video. And not just in the outbound, as known from well-known providers, but also in the inbound. This means that the customer can start a video call to the dealer using a button on the homepage. The call is then routed to the appropriate employee as with a correct telephone system according to previously defined rules (date, time, user groups).

For this application we need a landing page, which can later be translated into other languages. Screenshots of the application are included and additional ones can be created if required. As a technician, it is difficult for us to select the correct information here. So if there is a need for more information, we can certainly provide it if it is named.
Updates

I've made the mistake and made only a german briefing, which was really not suitable for the most designers. I've fixed this error and translated the briefing now.

Requirements
Must have
• A landing page design, for the new product. Please only designs which fits the topic and not some generic designs which need to be customized by us ... If we we're able to do this, we would not ask for help here ;-)
Should not have
• We do not need an admin template for the application, we already have an admin design.

```html
<!DOCTYPE html>
<html lang="en">
<head>
<meta charset="utf-8">
<title>FernHaven – Video Salesroom</title>
<link href="https://fonts.googleapis.com/css2?family=Open+Sans:wght@300;400;600;700&display=swap" rel="stylesheet">
<style>
  :root {
    --navy-deep: #0e1f33;
    --navy-mid: #1e3550;
    --indigo: #363a85;
    --card: #3a3d82;
    --step-1: #6470e0;
    --step-2: #4a4fb8;
    --step-3: #343a80;
    --accent-teal: #0f4a6e;
    --heading: #3d3d3d;
    --title: #2a2a2a;
    --body: #6a6a6a;
    --wave: #e4e4e4;
    --white: #ffffff;
    --sky-light: #e3ecf5;
    --sky-mid: #a9bfd6;
  }
  * { box-sizing: border-box; margin: 0; padding: 0; }
  html, body { width: 1200px; height: 750px; overflow: hidden; background: var(--white); }
  body { font-family: "Open Sans", sans-serif; position: relative; }

  .site-header {
    position: absolute; left: 0; top: 0; width: 1200px; height: 98px;
    background: linear-gradient(100deg, #2b3d55 0%, #5a5a4a 18%, #7a6c3c 24%, #34465c 38%, var(--navy-mid) 60%, var(--navy-deep) 100%);
  }
  .brand {
    position: absolute; left: 124px; top: 22px;
    font-size: 37px; font-weight: 600; color: var(--white); letter-spacing: 0.2px;
  }
  .main-nav a {
    position: absolute; top: 38px; color: var(--white); text-decoration: none;
    font-size: 15px; line-height: 22px; white-space: nowrap;
  }
  .nav-home { left: 628px; }
  .nav-software { left: 709px; }
  .nav-about { left: 848px; }
  .nav-contact { left: 929px; }
  .lang-switch {
    position: absolute; left: 1017px; top: 32px; width: 59px; height: 33px;
    border: 1px solid var(--white); border-radius: 3px; color: var(--white);
    font-size: 11px; display: flex; align-items: center; justify-content: center; gap: 4px;
  }

  .intro { position: absolute; left: 0; top: 98px; width: 634px; height: 652px; background: var(--white); overflow: hidden; }
  .intro-wave { position: absolute; left: 0; top: 0; }
  .headline {
    position: absolute; left: 124px; top: 28px;
    font-size: 33px; line-height: 41px; font-weight: 700; color: var(--heading); letter-spacing: 0.3px;
  }
  .headline .new { color: var(--accent-teal); }

  .feature { position: absolute; left: 127px; width: 500px; height: 60px; }
  .feature-num {
    position: absolute; left: 0; top: 0; width: 60px; height: 60px; border-radius: 50%;
    color: var(--white); font-size: 28px; font-weight: 600;
    display: flex; align-items: center; justify-content: center;
  }
  .feature-title {
    position: absolute; left: 85px; top: -1px; font-size: 21px; line-height: 28px;
    font-weight: 400; color: var(--title); white-space: nowrap;
  }
  .feature-title strong { font-weight: 700; }
  .feature-text {
    position: absolute; left: 86px; top: 27px; width: 345px;
    font-size: 15px; line-height: 20px; color: var(--body);
  }
  .feature-text.wide { width: 395px; }

  .btn { position: absolute; height: 40px; font-size: 15px; display: flex; align-items: center; justify-content: center; text-decoration: none; }
  .btn-primary { left: 214px; top: 543px; width: 120px; background: var(--indigo); color: var(--white); border-radius: 2px; }
  .btn-outline { left: 357px; top: 542px; width: 123px; height: 42px; border: 2px solid var(--indigo); color: var(--indigo); border-radius: 3px; background: var(--white); }

  .hero-visual {
    position: absolute; left: 634px; top: 98px; width: 566px; height: 652px;
    background: linear-gradient(135deg, var(--sky-mid) 0%, var(--sky-light) 35%, #f3f6fa 55%, #c7d6e6 80%, #8fa9c4 100%);
  }

  .subscribe-card {
    position: absolute; left: 697px; top: 358px; width: 389px; height: 302px;
    background: var(--card); border-radius: 0 45px 0 45px;
  }
  .subscribe-accent { position: absolute; left: 0; top: 53px; width: 58px; height: 7px; background: var(--white); }
  .subscribe-title {
    position: absolute; left: 0; top: 31px; width: 389px; padding-left: 10px; text-align: center;
    color: var(--white); font-size: 25px; font-weight: 300; line-height: 40px; letter-spacing: 0.5px;
  }
  .subscribe-title strong { font-weight: 700; }
  .email-field {
    position: absolute; left: 49px; top: 142px; width: 296px; height: 40px;
    background: var(--white); border-radius: 2px; color: #9a9a9a; font-size: 14px;
    display: flex; align-items: center; padding-left: 16px;
  }
  .subscribe-btn {
    position: absolute; left: 111px; top: 223px; width: 182px; height: 40px;
    background: var(--white); border-radius: 2px; color: var(--card); font-size: 15px;
    display: flex; align-items: center; justify-content: center;
  }
</style>
</head>
<body>
  <header class="site-header">
    <div class="brand">FernHaven</div>
    <nav class="main-nav">
      <a href="#" class="nav-home">Home</a>
      <a href="#" class="nav-software">Our Softwares</a>
      <a href="#" class="nav-about">About</a>
      <a href="#" class="nav-contact">Contact</a>
    </nav>
    <div class="lang-switch">
      <svg width="12" height="12" viewBox="0 0 12 12" aria-hidden="true">
        <circle cx="6" cy="6" r="5.5" fill="none" stroke="#fff" stroke-width="1"/>
        <path d="M3 3.5 Q5 3 5.5 5 Q4 6.5 4.5 8.5 M7.5 2 Q7 4 8.5 5 Q9.5 7 8 9.5" fill="none" stroke="#fff" stroke-width="1"/>
      </svg>
      <span>En</span><span>&#8964;</span>
    </div>
  </header>

  <section class="intro">
    <svg class="intro-wave" width="634" height="652" viewBox="0 0 634 652" aria-hidden="true">
      <path d="M0 577 C200 550 430 508 634 502 L634 652 L0 652 Z" fill="var(--wave)"/>
    </svg>
    <h1 class="headline">TRY OUR <span class="new">NEW</span> VIDEO<br>SALESROOM SOFTWARE</h1>

    <div class="feature" style="top:179px">
      <div class="feature-num" style="background:var(--step-1)">1</div>
      <h2 class="feature-title"><strong>Innovative</strong> software</h2>
      <p class="feature-text">Our solution can handle incoming calls from the website / shop / app of a customer.</p>
    </div>
    <div class="feature" style="top:280px">
      <div class="feature-num" style="background:var(--step-2)">2</div>
      <h2 class="feature-title"><strong>Appropriate</strong> call Routing</h2>
      <p class="feature-text wide">The call is routed by different rules to the correct sales agent.</p>
    </div>
    <div class="feature" style="top:401px">
      <div class="feature-num" style="background:var(--step-3)">3</div>
      <h2 class="feature-title"><strong>Excellent</strong> customer service</h2>
      <p class="feature-text wide">FernHaven has gained many satisfied customers.</p>
    </div>

    <a href="#" class="btn btn-primary">Get Started</a>
    <a href="#" class="btn btn-outline">More</a>
  </section>

  <div class="hero-visual" role="img" aria-label="Photo of bright modern architecture with diagonal blue-framed glass beams over a reflective floor"></div>

  <aside class="subscribe-card">
    <div class="subscribe-accent"></div>
    <h2 class="subscribe-title">BE <strong>UPDATED</strong> WITH<br>OUR PRODUCTS</h2>
    <div class="email-field">Email</div>
    <div class="subscribe-btn">Subscribe</div>
  </aside>
</body>
</html>
```